4 x Designs Required

Hi There,
I require 4 x different designs to be made for 4 new brands of mine however they can be quite interchangeable. HR Plinkr and Marketing Plinkr can be similar just with a difference in colour. The same goes for the Bulletin brands. This means there are ultimately two designs that need perfecting.

There must be a click here CTA on the banner somewhere. :-)

I require the banners in 728x90 format and 960x90 please.

Please use strap lines on the banners such as:
Essential Whitepapers for HR Professionals
Essential Whitepapers for Marketing Professionals
Your No.1 Whitepaper Resource

The brand names:
HR Plinkr
Marketing Plinkr
HR Dispatchly
Marketing Dispatchly

Examples attached.

```html
<!DOCTYPE html>
<html lang="en">
<head>
<meta charset="utf-8">
<title>Whitepaper Banner Set</title>
<link rel="stylesheet" href="https://fonts.googleapis.com/css2?family=Roboto:wght@400;500;700&display=swap">
<style>
  :root {
    --page-bg: #f5f5f5;
    --label-ink: #2a2a2a;
    --white: #ffffff;
    --ink-dark: #1f1f1f;
    --orange: #ff8c00;
    --cyan: #00e5ff;
    --link-blue: #1a8ad4;
    --navy-a: #0b2f52;
    --navy-b: #0a4570;
    --ocean-a: #0b5f8e;
    --ocean-b: #127aa8;
    --plum: #a23b7c;
    --violet: #4a2a96;
    --indigo: #1d2790;
    --flame: #ff3d22;
    --rose: #e8245a;
  }
  * { box-sizing: border-box; margin: 0; padding: 0; }
  html, body { width: 1200px; height: 919px; overflow: hidden; }
  body {
    position: relative;
    background: var(--page-bg);
    font-family: "Roboto", Arial, sans-serif;
  }
  .format-label {
    position: absolute;
    left: 0; width: 1200px;
    text-align: center;
    font-size: 20px;
    font-weight: 700;
    color: var(--label-ink);
    line-height: 24px;
  }
  .banner {
    position: absolute;
    height: 94px;
    border: 2px solid var(--white);
    box-shadow: 0 8px 12px rgba(0,0,0,0.28);
    overflow: hidden;
    color: var(--white);
  }
  .banner--leaderboard { left: 208px; width: 784px; }
  .banner--wide { left: 83px; width: 1034px; }
  .banner__backdrop { position: absolute; inset: 0; }
  .brand-name {
    position: absolute;
    font-weight: 500;
    white-space: nowrap;
    color: var(--white);
  }
  .brand-mark {
    position: absolute;
    width: 10px; height: 10px;
  }
  .headline {
    position: absolute;
    font-size: 15px;
    font-weight: 500;
    white-space: nowrap;
    line-height: 18px;
  }
  .strapline {
    position: absolute;
    font-size: 14px;
    font-weight: 400;
    white-space: nowrap;
    line-height: 18px;
  }
  .banner--wide .strapline { font-size: 17px; }
  .cta {
    position: absolute;
    top: 21px;
    height: 50px;
    border-radius: 3px;
    display: flex; align-items: center; justify-content: center;
    font-size: 12px;
    font-weight: 700;
    text-decoration: none;
  }
  .banner--leaderboard .cta { left: 614px; width: 130px; }
  .banner--wide .cta { left: 844px; width: 129px; box-shadow: 0 3px 6px rgba(0,0,0,0.2); background: var(--white); }
</style>
</head>
<body>

  <h2 class="format-label" style="top:90px">HR PLINKR (728X90)</h2>
  <div class="banner banner--leaderboard" style="top:140px">
    <div class="banner__backdrop" role="img" aria-label="Dark blue digital network imagery" style="background:linear-gradient(90deg,var(--navy-a),var(--navy-b) 55%,var(--navy-a))"></div>
    <span class="brand-mark" style="left:24px;top:41px;background:var(--orange)"></span>
    <span class="brand-name" style="left:40px;top:34px;font-size:20px">HR PLINKR</span>
    <p class="headline" style="left:187px;top:21px">ESSENTIAL WHITEPAPERS FOR HR PROFESSIONALS</p>
    <p class="strapline" style="left:188px;top:51px">Your No.1 Whitepaper Resource</p>
    <a class="cta" href="#" style="background:var(--orange);color:var(--white)">CLICK HERE</a>
  </div>

  <h2 class="format-label" style="top:287px">HR DISPATCHLY (728X90)</h2>
  <div class="banner banner--leaderboard" style="top:338px">
    <div class="banner__backdrop" role="img" aria-label="Bright blue connected network imagery" style="background:linear-gradient(90deg,var(--ocean-a),var(--ocean-b) 60%,var(--ocean-a))"></div>
    <span class="brand-mark" style="left:24px;top:41px;background:var(--cyan)"></span>
    <span class="brand-name" style="left:40px;top:34px;font-size:20px">HR Dispatchly</span>
    <p class="headline" style="left:187px;top:21px">ESSENTIAL WHITEPAPERS FOR HR PROFESSIONALS</p>
    <p class="strapline" style="left:188px;top:51px">Your No.1 Whitepaper Resource</p>
    <a class="cta" href="#" style="background:var(--cyan);color:var(--white)">CLICK HERE</a>
  </div>

  <h2 class="format-label" style="top:486px">MARKETING PLINKR (960X90)</h2>
  <div class="banner banner--wide" style="top:537px">
    <div class="banner__backdrop" role="img" aria-label="Purple to indigo abstract technology imagery" style="background:linear-gradient(90deg,var(--plum),var(--violet) 55%,var(--indigo))"></div>
    <span class="brand-name" style="left:55px;top:18px;font-size:13px;font-weight:700">MARKETING</span>
    <span class="brand-name" style="left:54px;top:32px;font-size:38px;font-weight:700">PLINKR</span>
    <p class="headline" style="left:262px;top:21px">ESSENTIAL WHITEPAPERS FOR MARKETING PROFESSIONALS</p>
    <p class="strapline" style="left:264px;top:49px">Your No.1 Whitepaper Resource</p>
    <a class="cta" href="#" style="color:var(--ink-dark)">CLICK HERE</a>
  </div>

  <h2 class="format-label" style="top:682px">MARKETING DISPATCHLY (960X90)</h2>
  <div class="banner banner--wide" style="top:733px">
    <div class="banner__backdrop" role="img" aria-label="Red orange imagery of a hand touching a circuit display" style="background:linear-gradient(90deg,var(--flame),#f0303c 45%,var(--rose))"></div>
    <span class="brand-name" style="left:55px;top:18px;font-size:21px;font-weight:700">MARKETING</span>
    <span class="brand-name" style="left:120px;top:47px;font-size:21px;font-weight:700">DISPATCHLY</span>
    <p class="headline" style="left:306px;top:21px">ESSENTIAL WHITEPAPERS FOR MARKETING PROFESSIONALS</p>
    <p class="strapline" style="left:308px;top:49px">Your No.1 Whitepaper Resource</p>
    <a class="cta" href="#" style="color:var(--link-blue)">CLICK HERE</a>
  </div>

</body>
</html>
```